Drizo-K.com Eliquid Bottling and insert flyer

Bottle:

We need a new bottle design; I have included the design but we are not hung up on the overall design.. We do not want it kid friendly tho! No cartoon graphics and things along those lines.

These must fit on an norvel standard 30 up label (2-5/8 x 1)
We want our name logo and brand name on the front. Along with a "space" where we can thermally print the e-juice name

Must have the following verbage on it

Contains
Nicotine, USP Propylene Glycol, USP Vegetable Glycerin, Artificial Food Grade Flavorings
Not for sale to minors
Made in the USA (Little USA Flag logo)
Shake well before use.
Keep out of reach
of children & Pets.

We would like options in small circles for nicotine levels, 24, 18, 9, 6,0 mg that we can use a small marker to highlight.

The juice brand is called "Brell'o Nectar"
Born on date is optional
The name needs to be in a area so we can custom print them via thermal printer

Insert:
We also need an insert announcing our company and a "XX" off coupon code We want a small spot where we can print the code along with the percentage
This will need to be in a standard format, 3x5 must have the domain name www.drizo-k.com and use the attached logos, everything else is full creativity

```html
<!DOCTYPE html>
<html lang="en">
<head>
<meta charset="utf-8">
<title>Drizo-K – Brell'o Nectar Bottle Label</title>
<link rel="stylesheet" href="https://fonts.googleapis.com/css2?family=Jost:wght@400;500;600;700;800&family=Open+Sans:wght@700;800&display=swap">
<style>
  :root {
    --purple: #6b3f9c;
    --purple-band: #7449ab;
    --purple-dark: #55307f;
    --purple-fold: #3f2262;
    --white: #ffffff;
    --backdrop: #e8e8e8;
    --ink: #111111;
    --red: #c8202a;
    --flag-red: #c8313a;
    --flag-blue: #2f3f86;
  }
  * { margin: 0; padding: 0; box-sizing: border-box; }
  html, body { width: 1200px; height: 806px; overflow: hidden; }
  body {
    background: var(--backdrop);
    font-family: "Jost", sans-serif;
    position: relative;
  }
  .label {
    position: absolute;
    left: 70px; top: 200px;
    width: 1060px; height: 405px;
    background: var(--white);
  }
  .side-panel {
    position: absolute; left: 0; top: 0;
    width: 317px; height: 405px;
  }
  .domain-bar {
    position: absolute; left: 0; top: 0;
    width: 317px; height: 58px;
    background: var(--purple);
    color: var(--white);
    font-weight: 700; font-size: 33px; letter-spacing: 0.5px;
    display: flex; align-items: center; justify-content: center;
  }
  .notice-list {
    position: absolute; left: 35px; top: 92px;
    list-style: none;
    color: var(--purple);
    font-size: 21px; line-height: 26px;
  }
  .notice-list li {
    position: relative; padding-left: 30px; margin-bottom: 12px;
  }
  .notice-list li svg {
    position: absolute; left: 0; top: 5px; width: 18px; height: 16px;
  }
  .brand-mark {
    display: flex; align-items: center; gap: 12px;
    color: var(--purple);
    font-weight: 600; font-size: 42px; line-height: 1;
    white-space: nowrap;
  }
  .brand-mark .dot {
    width: 30px; height: 30px; border-radius: 50%;
    background: var(--purple);
  }
  .side-panel .brand-mark { position: absolute; left: 44px; top: 257px; }
  .born-bar {
    position: absolute; left: 0; bottom: 0;
    width: 317px; height: 60px;
    background: var(--purple);
    color: var(--white);
    font-weight: 500; font-size: 20px; line-height: 23px;
    text-align: center;
    display: flex; flex-direction: column; justify-content: center;
  }
  .front-panel .brand-mark {
    position: absolute; left: 558px; top: 35px;
  }
  .ribbon {
    position: absolute; left: 363px; top: 58px;
    width: 652px; height: 150px;
  }
  .juice-name {
    position: absolute; left: 430px; top: 97px;
    width: 518px; height: 108px;
    display: flex; align-items: center; justify-content: center;
    color: var(--white);
    font-family: "Open Sans", sans-serif;
    font-weight: 800; font-size: 50px; letter-spacing: 0.5px;
    white-space: nowrap;
    text-shadow: 2px 3px 0 rgba(40,20,70,0.35);
  }
  .ingredients {
    position: absolute; left: 363px; top: 222px; width: 652px;
    text-align: center;
    color: var(--purple);
    font-family: "Open Sans", sans-serif; font-weight: 700;
    font-size: 16.5px; line-height: 24px;
  }
  .flag {
    position: absolute; left: 400px; top: 303px;
    width: 118px; height: 68px;
    background: linear-gradient(180deg, var(--flag-red) 0 14%, #fff 14% 28%, var(--flag-red) 28% 42%, #fff 42% 57%, var(--flag-red) 57% 71%, #fff 71% 85%, var(--flag-red) 85%);
  }
  .flag::before {
    content: ""; position: absolute; left: 0; top: 0;
    width: 50px; height: 38px; background: var(--flag-blue);
  }
  .made-in {
    position: absolute; left: 392px; top: 373px; width: 134px;
    text-align: center;
    font-family: "Open Sans", sans-serif; font-weight: 700;
    font-size: 15px; color: var(--ink);
  }
  .nicotine {
    position: absolute; left: 580px; top: 302px; width: 223px;
    text-align: center; color: var(--purple);
  }
  .nicotine-title { font-weight: 600; font-size: 18px; letter-spacing: 0.5px; }
  .nicotine-levels {
    display: flex; margin-top: 6px;
    height: 54px;
    border: 3px solid var(--purple); border-radius: 12px;
    overflow: hidden;
  }
  .nicotine-levels span {
    flex: 1; display: flex; align-items: center; justify-content: center;
    font-size: 21px;
    border-right: 2px solid var(--purple);
  }
  .nicotine-levels span:last-child { border-right: 0; }
  .age-sign {
    position: absolute; left: 880px; top: 300px;
    width: 94px; height: 94px;
  }
</style>
</head>
<body>
  <div class="label">
    <section class="side-panel">
      <div class="domain-bar">DRIZO-K.COM</div>
      <ul class="notice-list">
        <li><svg viewBox="0 0 18 16"><path d="M1 9 L6 14 L17 1" fill="none" stroke="#6b3f9c" stroke-width="3"/></svg>Shake well before use</li>
        <li><svg viewBox="0 0 18 16"><path d="M1 9 L6 14 L17 1" fill="none" stroke="#6b3f9c" stroke-width="3"/></svg>Not for sale to minors</li>
        <li><svg viewBox="0 0 18 16"><path d="M1 9 L6 14 L17 1" fill="none" stroke="#6b3f9c" stroke-width="3"/></svg>Keep out of reach<br>of children &amp; Pets</li>
      </ul>
      <div class="brand-mark"><span>Drizo-K</span><span class="dot"></span></div>
      <div class="born-bar"><span>Born on date</span><span>mm/dd/yy</span></div>
    </section>

    <section class="front-panel">
      <div class="brand-mark"><span>Drizo-K</span><span class="dot"></span></div>
      <svg class="ribbon" viewBox="0 0 652 150" aria-hidden="true">
        <polygon points="0,2 122,2 122,117 0,117 38,60" fill="var(--purple-dark)"/>
        <polygon points="652,2 530,2 530,117 652,117 614,60" fill="var(--purple-dark)"/>
        <polygon points="67,117 122,117 122,147" fill="var(--purple-fold)"/>
        <polygon points="585,117 530,117 530,147" fill="var(--purple-fold)"/>
        <rect x="67" y="39" width="518" height="108" fill="var(--purple-band)"/>
        <rect x="67" y="45" width="518" height="96" fill="none" stroke="rgba(255,255,255,0.35)" stroke-width="1.5" stroke-dasharray="4 3"/>
      </svg>
      <div class="juice-name">BRELL'O NECTAR</div>
      <p class="ingredients">Contains<br>Nicotine, USP Propylene Glycol, USP Vegetable Glycerin,<br>Artificial Food Grade Flavorings</p>
      <div class="flag" role="img" aria-label="Small United States flag"></div>
      <div class="made-in">Made in USA</div>
      <div class="nicotine">
        <div class="nicotine-title">NICOTINE LEVELS</div>
        <div class="nicotine-levels"><span>24</span><span>18</span><span>9</span><span>6</span><span>0</span></div>
      </div>
      <svg class="age-sign" viewBox="0 0 94 94" role="img" aria-label="Not for under 18 sign">
        <circle cx="47" cy="47" r="41" fill="#fff" stroke="var(--red)" stroke-width="8"/>
        <text x="47" y="33" text-anchor="middle" font-family="Open Sans, sans-serif" font-weight="700" font-size="7" fill="var(--ink)">UNDER</text>
        <text x="47" y="68" text-anchor="middle" font-family="Open Sans, sans-serif" font-weight="800" font-size="38" fill="var(--ink)">18</text>
        <line x1="18" y1="18" x2="76" y2="76" stroke="var(--red)" stroke-width="8"/>
      </svg>
    </section>
  </div>
</body>
</html>
```